We (R. T. Halvering & Associates, Inc.) are an executive Search firm based in Los Angeles that is exclusively focused in the Med Tech and Health Tech arenas.   I need a logo to communicate that we are a high end search firm, but also that we are focused in the medicine and science arenas called health tech and med tech.  Many of our clients have robotics and artificial intelligence type products, so it is very technology forward.  I tend to gravitate towards clean, sharp aesthetic as opposed to something that is really over the top.
Attached are files with my logo in two different layouts.  In addition to the letterhead and envelope, I also will need an electronic letterhead in Microsoft Word.  I tend to
I look forward to seeing the designs and just let me know if you have any questions.
Dale

```html
<!DOCTYPE html>
<html lang="en">
<head>
<meta charset="utf-8">
<title>R. T. Halvering &amp; Associates, Inc. — Letterhead</title>
<link href="https://fonts.googleapis.com/css2?family=Open+Sans:wght@400;600&family=Roboto:wght@400&display=swap" rel="stylesheet">
<style>
  :root {
    --backdrop: #dedede;
    --paper: #f8f8f8;
    --ink: #111111;
    --body-text: #666666;
    --footer-text: #555555;
    --brand-blue: #4a9bd4;
    --signature-tone: #dfe5ee;
  }
  * { margin: 0; padding: 0; box-sizing: border-box; }
  html, body {
    width: 1153px; height: 1200px; overflow: hidden;
    background: var(--backdrop);
  }
  .letterhead {
    position: absolute; left: 181px; top: 50px;
    width: 791px; height: 1100px;
    background: var(--paper);
    box-shadow: 0 6px 24px rgba(0,0,0,0.12);
    font-family: "Open Sans", sans-serif;
    color: var(--body-text);
  }
  .brand {
    position: absolute; left: 0; right: 0; top: 96px;
    display: flex; align-items: center; justify-content: center; gap: 14px;
  }
  .brand-dot { width: 34px; height: 34px; border-radius: 50%; background: var(--brand-blue); }
  .brand-name {
    font-family: "Open Sans", sans-serif; font-weight: 600;
    font-size: 22px; letter-spacing: 0.5px; color: var(--ink);
  }
  .letter {
    position: absolute; left: 71px; top: 242px; width: 648px;
    font-size: 14px; line-height: 21px; letter-spacing: 0.1px;
  }
  .letter p { text-align: justify; margin-bottom: 21px; }
  .letter .salutation { text-align: left; }
  .letter .closing { text-align: left; margin-bottom: 0; }
  .signature {
    position: absolute; left: 71px; top: 803px; width: 91px; height: 86px;
    background: var(--signature-tone); border-radius: 4px;
  }
  .contact {
    position: absolute; left: 71px; top: 984px;
    font-family: "Roboto", sans-serif; font-size: 17px; line-height: 22px;
    color: var(--footer-text); list-style: none;
  }
  .contact li { display: flex; align-items: center; gap: 6px; }
  .contact svg { width: 16px; height: 16px; flex: none; }
  .address {
    position: absolute; right: 73px; top: 987px; text-align: right;
    font-family: "Roboto", sans-serif; font-size: 17px; line-height: 22px;
    color: var(--footer-text); font-style: normal;
  }
  .address .company { color: var(--brand-blue); }
</style>
</head>
<body>
  <main class="letterhead">
    <header class="brand">
      <span class="brand-dot"></span>
      <span class="brand-name">R. T. HALVERING &amp; ASSOCIATES, INC.</span>
    </header>

    <section class="letter">
      <p class="salutation">Dear customer,</p>
      <p>Lorem ipsum dolor sit amet, consectetur adipisicing elit, sed do eiusmod tempor incididunt ut labore et dolore magna aliqua. Ut enim ad minim veniam, quis nostrud exercitation ullamco laboris nisi ut aliquip ex ea commodo consequat. Duis aute irure dolor in reprehenderit in voluptate velit esse cillum dolore eu fugiat nulla pariatur. Excepteur sint occaecat cupidatat non proident, sunt in culpa qui officia deserunt mollit anim id est laborum.</p>
      <p>Lorem ipsum dolor sit amet, consectetur adipisicing elit, sed do eiusmod tempor incididunt ut labore et dolore magna aliqua. Ut enim ad minim veniam, quis nostrud exercitation ullamco laboris nisi ut aliquip ex ea commodo consequat. Duis aute irure dolor in reprehenderit in voluptate velit esse cillum dolore eu fugiat nulla pariatur. Excepteur sint occaecat cupidatat non proident, sunt in culpa qui officia deserunt mollit anim id est laborum.</p>
      <p>Lorem ipsum dolor sit amet, consectetur adipisicing elit, sed do eiusmod tempor incididunt ut labore et dolore magna aliqua. Ut enim ad minim veniam, quis nostrud exercitation ullamco laboris nisi ut aliquip ex ea commodo consequat. Duis aute irure dolor in reprehenderit in voluptate velit esse cillum dolore eu fugiat nulla pariatur. Excepteur sint occaecat cupidatat non proident, sunt in culpa qui officia deserunt mollit anim id est laborum.</p>
      <p>Lorem ipsum dolor sit amet, consectetur adipisicing elit, sed do eiusmod tempor incididunt ut labore et dolore magna aliqua. Ut enim ad minim veniam, quis nostrud exercitation ullamco laboris nisi ut aliquip ex ea commodo consequat. Duis aute irure dolor in reprehenderit.</p>
      <p class="closing">Yours Sincerely,</p>
    </section>

    <div class="signature" role="img" aria-label="Handwritten signature"></div>

    <ul class="contact">
      <li>
        <svg viewBox="0 0 16 16" aria-hidden="true"><path fill="#4a9bd4" d="M3.6 1.2l2.3 2.6c.4.4.4 1-.1 1.4L4.7 6.3c.9 2 2.9 4 5 5l1.1-1.1c.4-.4 1-.4 1.4 0l2.6 2.3c.4.4.4 1 0 1.4l-1.3 1.3c-.6.6-1.6.8-2.4.4C6.7 14 2 9.3.4 4.9.1 4 .3 3 .9 2.4L2.2 1.2c.4-.4 1-.4 1.4 0z"/></svg>
        +13105550147
      </li>
      <li>
        <svg viewBox="0 0 16 16" aria-hidden="true"><rect x="0.5" y="3" width="15" height="10" fill="#4a9bd4"/><path d="M1 3.5l7 5.5 7-5.5" fill="none" stroke="#f8f8f8" stroke-width="1.2"/></svg>
        info@rthalvering.com
      </li>
      <li>
        <svg viewBox="0 0 16 16" aria-hidden="true"><g fill="none" stroke="#4a9bd4" stroke-width="1.2"><circle cx="8" cy="8" r="7"/><ellipse cx="8" cy="8" rx="3" ry="7"/><path d="M1 8h14M2.5 4h11M2.5 12h11"/></g></svg>
        www.rthalvering.com
      </li>
    </ul>

    <address class="address">
      <span class="company">R. T. Halvering &amp; Associates, Inc.</span><br>
      48 Crescent Ridge Way,<br>
      Los Angeles, CA 90025
    </address>
  </main>
</body>
</html>
```